Postcard, Logo, and Website Design for Direct to Consumer Personal Bankruptcy Service

We are launching a bankruptcy legal practice. Our postcard design will be mailed to prospective clients who have already been sued by their credit card companies.

We would like people to glean from the post card that they can call to set up a no-fee consultation, or to phone our offices, where our receptionist can aid them in setting up a no-fee consultation.

Logo should be professional, but not overly stuffy.

Website copy can be added later, but most important is a space where people can fill out there info so we can reach out to them.

Pertinent info that should be on postcard

Name: Harbor Pines Debt Relief
Phone: 616-392-7158
Website: HPDebtRelief.example

Rough ideas that we've tossed around include the following (but use your own judgement - we're counting on you for creativity):

Creditors Calling?
Mountain of Debt?
Getting Sued?

We can help!

Target Market(s)

People who are thinking about bankruptcy and have already been sued

Industry/Entity Type

Financial Service

Logo Text

Harbor Pines Debt Relief

Number of Pages Required

1 page

Font styles to use
Sans Serif

Colors

Designer to choose colors to be used in the design.

Requirements
Must have
• Space for info about bankruptcy process
• Space for user to submit info

```html
<!DOCTYPE html>
<html lang="en">
<head>
<meta charset="utf-8">
<title>Harbor Pines Debt Relief – Postcard</title>
<link href="https://fonts.googleapis.com/css2?family=Arimo:wght@400;700&display=swap" rel="stylesheet">
<style>
  :root{
    --backdrop:#444546;
    --card:#ffffff;
    --teal:#35bcb1;
    --navy:#1e3a56;
    --ink:#222a33;
    --black:#1d1c1e;
    --photo-warm:#c9a57a;
    --photo-dark:#5a4c40;
    --stamp:#c8c8c8;
  }
  *{margin:0;padding:0;box-sizing:border-box}
  html,body{width:850px;height:1200px;overflow:hidden}
  body{background:var(--backdrop);font-family:"Arimo",Arial,sans-serif;position:relative}
  .card{position:absolute;left:114px;width:621px;height:401px;background:var(--card);
        box-shadow:0 8px 18px rgba(0,0,0,.45);overflow:hidden}
  .card--front{top:153px}
  .card--back{top:715px}
  .card__shapes{position:absolute;inset:0}
  .abs{position:absolute}
  .brand-name{color:var(--teal);font-weight:400;white-space:nowrap}
  .brand-dot{display:inline-block;width:10px;height:10px;border-radius:50%;background:var(--teal);margin-right:6px;vertical-align:middle}

  /* front */
  .front__brand{left:23px;top:82px;font-size:17px}
  .questions{left:21px;top:106px;list-style:none;color:var(--navy);font-size:17px;line-height:25px}
  .questions li{display:flex;align-items:center}
  .questions .num{display:inline-flex;align-items:center;justify-content:center;width:15px;height:15px;border-radius:50%;
       background:var(--navy);color:#fff;font-size:11px;font-weight:700;margin-right:7px}
  .questions b{font-weight:700}
  .headline{left:20px;top:178px;color:var(--navy);font-size:35px;font-weight:400;letter-spacing:-.3px}
  .subhead{left:20px;top:225px;width:230px;font-size:11.5px;color:var(--ink);line-height:14px}
  .intro{left:20px;top:261px;width:225px;font-size:8.6px;color:var(--ink);line-height:11px}
  .call-label{left:20px;top:322px;color:var(--teal);font-size:18px;font-weight:700}
  .front__phone{left:20px;top:359px;display:flex;align-items:center;color:#fff;font-size:20px;font-weight:700}
  .icon-ring{width:24px;height:24px;margin-right:10px}
  .front__firm{left:260px;top:304px;width:361px;text-align:center;color:#fff;font-size:24px}
  .front__globe{left:427px;top:340px;width:22px;height:22px}
  .front__site{left:260px;top:363px;width:361px;text-align:center;color:#fff;font-size:22px}

  /* back */
  .back__firm{left:23px;top:30px;color:#fff;font-size:19px}
  .back__title{left:23px;top:59px;color:#fff;font-size:25px}
  .back__rule{left:23px;top:90px;width:158px;height:1px;background:#fff}
  .back__copy{left:23px;top:99px;width:205px;color:#fff;font-size:10.8px;line-height:12.6px}
  .back__copy p+p{margin-top:12px}
  .back__copy strong{text-transform:uppercase}
  .back__brand{left:400px;top:68px;font-size:13px}
  .stamp{left:531px;top:20px;width:60px;height:60px;border:1.5px solid var(--stamp)}
  .contact{display:flex;align-items:center;color:#fff}
  .back__site{left:21px;top:324px;font-size:18px}
  .back__phone{left:21px;top:360px;font-size:20px;font-weight:700}
</style>
</head>
<body>

<!-- Front -->
<section class="card card--front">
  <svg class="card__shapes" width="621" height="401" viewBox="0 0 621 401">
    <defs>
      <linearGradient id="libraryTone" x1="0" y1="0" x2="1" y2="1">
        <stop offset="0" stop-color="#b9a48a"/>
        <stop offset=".5" stop-color="#d8cbb8"/>
        <stop offset="1" stop-color="#7b5a40"/>
      </linearGradient>
    </defs>
    <polygon points="251,0 272,0 366,277 356,277" fill="var(--teal)"/>
    <polygon role="img" aria-label="Photo of law books, a gavel and scales of justice on a library shelf"
             points="272,0 621,0 621,277 366,277" fill="url(#libraryTone)"/>
    <polygon points="264,278 521,278 516,291 259,291" fill="var(--navy)"/>
    <polygon points="258,284 621,284 621,401 219,401" fill="var(--teal)"/>
    <polygon points="0,343 241,343 219,401 0,401" fill="var(--black)"/>
  </svg>

  <div class="abs front__brand brand-name"><span class="brand-dot"></span>HPDebtRelief</div>
  <ol class="abs questions">
    <li><span class="num">1</span>Creditors&nbsp;<b>CALLING?</b></li>
    <li><span class="num">2</span>Mountain of&nbsp;<b>DEBT?</b></li>
    <li><span class="num">3</span>Getting&nbsp;<b>SUED?</b></li>
  </ol>
  <h1 class="abs headline">We can help!</h1>
  <p class="abs subhead">YOU HAVE OPTIONS FOR GETTING OUT OF DEBT!</p>
  <p class="abs intro">Bad things happen to everyone. When you're facing financial hardship, it's how you resolve your debt that counts. We strive to help our clients do just that - bounce back from financial distress and achieve their goals.</p>
  <p class="abs call-label">Call us:</p>
  <div class="abs front__phone">
    <svg class="icon-ring" viewBox="0 0 24 24"><circle cx="12" cy="12" r="11" fill="none" stroke="#fff" stroke-width="1.5"/><path d="M8.5 6.5l2 2.5-1.2 1.3c.8 1.7 2 2.9 3.6 3.7l1.3-1.2 2.5 2-1.4 1.8c-4-.8-7.2-4-8.1-8.2z" fill="#fff"/></svg>
    616-392-7158
  </div>
  <p class="abs front__firm">Harbor Pines Debt Relief</p>
  <svg class="abs front__globe" viewBox="0 0 22 22" fill="none" stroke="#fff" stroke-width="1.3"><circle cx="11" cy="11" r="9.5"/><ellipse cx="11" cy="11" rx="4.2" ry="9.5"/><path d="M1.5 11h19M3 6h16M3 16h16"/></svg>
  <p class="abs front__site">HPDebtRelief.example</p>
</section>

<!-- Back -->
<section class="card card--back">
  <svg class="card__shapes" width="621" height="401" viewBox="0 0 621 401">
    <defs>
      <linearGradient id="officeTone" x1="0" y1="0" x2="1" y2="1">
        <stop offset="0" stop-color="var(--photo-dark)"/>
        <stop offset=".6" stop-color="#7d6956"/>
        <stop offset="1" stop-color="var(--photo-warm)"/>
      </linearGradient>
    </defs>
    <polygon role="img" aria-label="Blurred photo of an attorney at a desk with scales of justice"
             points="0,0 318,0 226,270 0,270" fill="url(#officeTone)"/>
    <polygon points="304,0 344,0 257,220 222,220" fill="var(--navy)"/>
    <polygon points="326,0 344,0 263,220 257,220" fill="var(--teal)" opacity=".9"/>
    <polygon points="0,288 204,288 199,302 0,302" fill="var(--navy)"/>
    <polygon points="0,296 238,296 284,401 0,401" fill="var(--teal)"/>
  </svg>

  <p class="abs back__firm">Harbor Pines Debt Relief</p>
  <h2 class="abs back__title">About us</h2>
  <div class="abs back__rule"></div>
  <div class="abs back__copy">
    <p>As attorneys, we will consider your entire financial situation and provide you with options to overcome debt that you feel comfortable with.</p>
    <p>If you want to end your increasing debt distress, take control of your financial situation, and improve your credit, <strong>call us to schedule a free no-obligation consultation!"</strong></p>
  </div>
  <div class="abs back__brand brand-name"><span class="brand-dot"></span>HPDebtRelief</div>
  <div class="abs stamp"></div>
  <div class="abs contact back__site">
    <svg class="icon-ring" viewBox="0 0 24 24" fill="none" stroke="#fff" stroke-width="1.3"><circle cx="12" cy="12" r="11"/><circle cx="12" cy="12" r="7"/><ellipse cx="12" cy="12" rx="3" ry="7"/><path d="M5 12h14M6 8.5h12M6 15.5h12"/></svg>
    HPDebtRelief.example
  </div>
  <div class="abs contact back__phone">
    <svg class="icon-ring" viewBox="0 0 24 24"><circle cx="12" cy="12" r="11" fill="none" stroke="#fff" stroke-width="1.5"/><path d="M8.5 6.5l2 2.5-1.2 1.3c.8 1.7 2 2.9 3.6 3.7l1.3-1.2 2.5 2-1.4 1.8c-4-.8-7.2-4-8.1-8.2z" fill="#fff"/></svg>
    616-392-7158
  </div>
</section>

</body>
</html>
```